Tidewell Oyster-new seafood raw bar restaurant menu

We are a Local Seafood & Raw Bar restaurant that is looking to open in 3 months. I need-Dinner Menu Design, Happy Hour Menu, Cocktail Menu, Brunch Menu, Lunch Menu. I'd like to have you start w/ the dinner menu first then whomever I choose will also do the rest of my menus. The SHELLHOUSE by Kelpcove menu is the direction im going for as far as font organization. Id like you to give us our own personal touch. Ive also provided a mock menu that a local designer started that can't finish due to timing.

Target Market(s)

mid to high end casual seafood restaurant

Industry/Entity Type

restaurant

Font styles to use
Serif
Sans Serif

Colors
0054AA
0677BA
7BADD7
CADEEF
E8F1F8
0094D4
00A9DD
6FCCEA
C7EBF8
E9F6FB
00AB8E
00BBA5
67D7C9
C6EFE9
E9F9F6

Requirements
Must have
• 11" x 14" size

```html
<!DOCTYPE html>
<html lang="en">
<head>
<meta charset="utf-8">
<title>Tidewell Oyster – Dinner Menu</title>
<link rel="stylesheet" href="https://fonts.googleapis.com/css2?family=Josefin+Sans:wght@400;600&family=Libre+Baskerville:wght@400;700&family=Parisienne&family=Amatic+SC:wght@400;700&display=swap">
<style>
  :root {
    --navy: #0f3f87;
    --teal: #5ec8d6;
    --ink: #ffffff;
    --paper: #ffffff;
    --rope: #2a5ea8;
    --art: #dfe9f4;
  }
  * { margin: 0; padding: 0; box-sizing: border-box; }
  html, body { width: 1200px; height: 880px; overflow: hidden; background: var(--paper); }
  .menu { position: relative; width: 1200px; height: 880px; background: var(--paper); }

  .rope { position: absolute; left: 35px; width: 1132px; height: 10px; background: var(--rope); border-radius: 5px; }
  .rope--top { top: 22px; }
  .rope--bottom { top: 852px; }

  .brand { position: absolute; left: 520px; top: 44px; width: 160px; height: 116px; text-align: center; }
  .brand__dot { width: 14px; height: 14px; border-radius: 50%; background: var(--navy); margin: 22px auto 10px; }
  .brand__name { font-family: "Josefin Sans", sans-serif; font-weight: 600; font-size: 20px; letter-spacing: 2px; color: var(--navy); text-transform: uppercase; line-height: 1.15; }

  .panel { position: absolute; background: var(--navy); color: var(--ink); }
  .panel--smaller { left: 40px; top: 78px; width: 347px; height: 727px; }
  .panel--raw { left: 427px; top: 176px; width: 345px; height: 629px; }
  .panel--signatures { left: 814px; top: 80px; width: 342px; height: 728px; }

  .panel__art { position: absolute; top: 0; right: 0; width: 94px; height: 86px; background: var(--art); opacity: .9; }

  .section-title { position: absolute; font-family: "Josefin Sans", sans-serif; font-weight: 400; color: var(--teal); letter-spacing: 3px; text-transform: uppercase; }
  .panel--smaller .section-title { left: 18px; top: 44px; font-size: 32px; }
  .panel--raw .section-title { left: 0; width: 100%; top: 16px; text-align: center; font-size: 31px; line-height: 1.05; }
  .section-title--script { left: 18px; top: 24px; font-family: "Parisienne", cursive; font-size: 42px; letter-spacing: 0; text-transform: none; }
  .section-title--desserts { left: 20px; top: 632px; font-size: 30px; }

  .item { position: absolute; left: 16px; right: 12px; }
  .panel--raw .item { left: 22px; }
  .panel--signatures .item { left: 18px; }
  .item__name { font-family: "Josefin Sans", sans-serif; font-weight: 400; font-size: 16px; letter-spacing: 1.2px; text-transform: uppercase; line-height: 1.05; white-space: nowrap; }
  .item__name--long { letter-spacing: .6px; }
  .item__desc { font-family: "Libre Baskerville", serif; font-size: 10.5px; letter-spacing: -.2px; line-height: 1.3; }

  .kids { position: absolute; left: 6px; top: 502px; width: 333px; height: 120px; background: var(--paper); color: var(--navy); overflow: hidden; }
  .kids__title { position: absolute; left: 16px; top: 2px; font-family: "Amatic SC", sans-serif; font-weight: 400; font-size: 40px; color: var(--teal); letter-spacing: 1px; line-height: 1.1; }
  .kids__list { position: absolute; left: 16px; top: 50px; list-style: none; font-family: "Josefin Sans", sans-serif; font-size: 15px; letter-spacing: 1.2px; line-height: 16px; }
  .kids__art { position: absolute; right: 4px; bottom: 4px; width: 92px; height: 86px; background: var(--navy); opacity: .85; }

  .desserts { position: absolute; left: 18px; top: 670px; list-style: none; font-family: "Josefin Sans", sans-serif; font-weight: 600; font-size: 16px; letter-spacing: 1.2px; line-height: 1.05; }
</style>
</head>
<body>
<main class="menu">
  <div class="rope rope--top"></div>

  <header class="brand">
    <div class="brand__dot"></div>
    <div class="brand__name">Tidewell<br>Oyster</div>
  </header>

  <section class="panel panel--smaller">
    <div class="panel__art" role="img" aria-label="Anchor illustration"></div>
    <h2 class="section-title">Smaller</h2>
    <div class="item" style="top:96px"><div class="item__name">Fried Shrimp</div><div class="item__desc">Remoulade</div></div>
    <div class="item" style="top:150px"><div class="item__name">Mussels</div><div class="item__desc">Local bacon, shallot, garlic, tomato, spicy herb butter</div></div>
    <div class="item" style="top:201px"><div class="item__name">Roasted Oysters</div><div class="item__desc">½ dozen, Choice of Rockefeller, Bienville, Tidewell special</div></div>
    <div class="item" style="top:256px"><div class="item__name">Shrimp and Grits</div><div class="item__desc">Local andouille, roasted peppers, garlic,<br>shallot, charred tomato</div></div>
    <div class="item" style="top:314px"><div class="item__name">Crab Mac’n Cheese</div><div class="item__desc">Cheddar, fontina, cotija, local pasta shells</div></div>
    <div class="item" style="top:358px"><div class="item__name">Shrimp Remoulade</div><div class="item__desc">Avocado, fried green tomato</div></div>
    <div class="item" style="top:410px"><div class="item__name">Pumpkin Risotto</div><div class="item__desc">Herbs, dried cherry, local mushrooms</div></div>
    <div class="item" style="top:465px"><div class="item__name">Caeser</div><div class="item__desc">Baby gem lettuce, parmesan</div></div>
    <div class="item" style="top:516px"><div class="item__name item__name--long">Skyrow Farms Crisp Greens Salad</div><div class="item__desc">Fig, goat cheese, spiced pepitos, sour cherry vinaigrette</div></div>
    <div class="item" style="top:568px"><div class="item__name">Clam Chowder</div><div class="item__desc">New England style</div></div>
    <div class="item" style="top:625px"><div class="item__name">Baja Fish Tacos</div><div class="item__desc">Slaw, cilantro, lime</div></div>
    <div class="item" style="top:684px"><div class="item__name">Steak Taco</div><div class="item__desc">Mojo, dried chili salsa, pickled onion, cotija</div></div>
  </section>

  <section class="panel panel--raw">
    <h2 class="section-title">Raw Bar/Chilled<br>Seafood</h2>
    <div class="item" style="top:109px"><div class="item__name">Oyster Chef’s Preparation</div></div>
    <div class="item" style="top:138px"><div class="item__name">Oyster Selection</div><div class="item__desc">House &nbsp;&nbsp;&nbsp;$ &nbsp;&nbsp;&nbsp;&nbsp;East Coast &nbsp;&nbsp;$<br>Regional $<br><span style="display:block;margin-top:3px">Accompaniments, top’em</span></div></div>
    <div class="item" style="top:210px"><div class="item__name">Seafood Tower</div><div class="item__desc">Small<br>Large<br>Build Your own</div></div>
    <div class="item" style="top:278px"><div class="item__name">Ceviche</div><div class="item__desc">Citrus, fruit, peppers, onion, cilantro</div></div>
    <div class="item" style="top:318px"><div class="item__name">Tuna Poke/Crudo</div><div class="item__desc">Ponzu, scallions, ginger, avocado, sesame</div></div>
    <div class="item" style="top:356px"><div class="item__name">Scallop Crudo</div><div class="item__desc">Lemon, ginger, chives, olive oil, pine nuts</div></div>
    <div class="item" style="top:394px"><div class="item__name">Peel and Eat Shrimp</div><div class="item__desc">Remoulade, tartar, cocktail</div></div>
    <div class="item" style="top:438px"><div class="item__name">Local Fish Crudo</div><div class="item__desc">Seasonal accompaniments</div></div>
    <div class="item" style="top:480px"><div class="item__name">Cured Salmon</div></div>

    <div class="kids">
      <h3 class="kids__title">Kids Menu</h3>
      <ul class="kids__list">
        <li>CHICKEN TENDERS</li>
        <li>MAC N CHEESE</li>
        <li>FRIED FISH</li>
        <li>FRIED SHRIMP</li>
      </ul>
      <div class="kids__art" role="img" aria-label="Anchor illustration"></div>
    </div>
  </section>

  <section class="panel panel--signatures">
    <div class="panel__art" role="img" aria-label="Anchor illustration"></div>
    <h2 class="section-title section-title--script">Signatures</h2>
    <div class="item" style="top:89px"><div class="item__name">Clam Linguini</div><div class="item__desc">Local Pasta. Local Bacon, peppers, butter, herbs</div></div>
    <div class="item" style="top:129px"><div class="item__name">Vegetable Gnocchi</div><div class="item__desc">Squash, shallots, peas, mushroom, basil, parmesan</div></div>
    <div class="item" style="top:169px"><div class="item__name">Pan Seared Scallops</div><div class="item__desc">Curry, cauliflower, carrots, eggplant, Carolina gold rice</div></div>
    <div class="item" style="top:209px"><div class="item__name">Halibut Gumbo</div><div class="item__desc">Shrimp, scallions, okra garnish</div></div>
    <div class="item" style="top:249px"><div class="item__name">Grilled Steak</div><div class="item__desc">Roasted rainbow carrots, mashed potatoes, ancho demi, chimichurri</div></div>
    <div class="item" style="top:302px"><div class="item__name">Surf and Turf Filet</div><div class="item__desc">Asparagus, baby potatoes, bearnaise, demi</div></div>
    <div class="item" style="top:350px"><div class="item__name">Fresh Catch</div></div>
    <div class="item" style="top:382px"><div class="item__name">Crab Legs</div><div class="item__desc">Butter, cocktail, spicy remoulade</div></div>
    <div class="item" style="top:422px"><div class="item__name">Lowcountry Boil</div><div class="item__desc">Shrimp, sausage, corn, potato</div></div>
    <div class="item" style="top:462px"><div class="item__name">Smash Burger</div><div class="item__desc">Spicy “thousand Island”, pickles, house cut fries, LTO</div></div>
    <div class="item" style="top:502px"><div class="item__name">Lobster Roll</div><div class="item__desc">Lots of Lobstah, scallions, celery, house fries</div></div>
    <div class="item" style="top:542px"><div class="item__name">Fish Sandwich</div><div class="item__desc">Double stacked halibut, pickled carrots, Lemon/caper/dill aioli, lettuce, tomato</div></div>

    <h2 class="section-title section-title--desserts">Desserts</h2>
    <ul class="desserts">
      <li>CHOCOLATE</li>
      <li>RASPBERRY</li>
      <li>BLUE</li>
    </ul>
  </section>

  <div class="rope rope--bottom"></div>
</main>
</body>
</html>
```